Accountant website

Please design a accountant website for www.fenwaylodgeadvisory.com.au. This site is majorly out of date, and is not supported by modern browsers.

The style should use the reds from the design at dev.fenwaylodgeadvisory.com.au, and should be modern and make use of Slides (large content slides that the user scrolls through on the front page).

The content is largely already on the site, however happy to move some around to suit the modern design as required.

The dev.fenwaylodgeadvisory.com.au was a rough mock up that I have completed that the client is "happy" with the direction, however this needs a lot of polish and finishing touches, and I will accept designs that differ from this, but highly recommend that this is used as a guide.

Ready to be sliced PSD Only - HTML no required.

In all honesty, although I can technically do a lot of this, the polished finished I want for this site has eluded me in a few attempts, and therefore I am looking out there at you much more artistic people to finish (or redesign if required) this site.

Target Market(s)

Higher end Small - Medium Business

Industry/Entity Type

Accountant

Requirements
Must have
• Must use the logo from dev.fenwaylodgeadvisory.com.au use exactly the red colours as defined in this layout. A basic layout PSD (to get the colour etc) and the logo in ai format is attached to this project. Please ignore the SSL warning on the development site.

The final product does NOT have to be the same as shown on dev.fenwaylodgeadvisory.com.au however the red colour scheme must be used. The client DOES want the logo on the RIGHT.

Must have a front landing page design, and a page layout that considers the other page content (at least one separate PSD)
Nice to have
• I really am looking at a slide format for the front page simular to:

http://www.plumvine.com/au/
http://www.tidelockbox.com/

The attached photos should be used on the site. Was considering a rotating banner with these images are a watermark background on a solid Red header bar, but happy to be shown other options.
Should not have
• Please no "Pattern Goblin" submissions.

```html
<!DOCTYPE html>
<html lang="en">
<head>
<meta charset="utf-8">
<title>Fenway Lodge Advisory</title>
<link href="https://fonts.googleapis.com/css2?family=Roboto:ital,wght@0,300;0,400;0,500;1,400&display=swap" rel="stylesheet">
<style>
:root{
  --red:#d9262f;
  --red-deep:#b81d26;
  --ink:#222;
  --text:#3a3a3a;
  --muted:#666;
  --panel:#f7f7f7;
  --footer:#1c1d1f;
  --white:#fff;
}
*{box-sizing:border-box;margin:0;padding:0}
html,body{width:943px;height:1200px;overflow:hidden;background:var(--white)}
body{position:relative;font-family:"Roboto",sans-serif;color:var(--text)}
.abs{position:absolute}

/* header */
.call{left:92px;top:18px}
.call-label{font-size:13px;color:#444;margin-left:24px}
.call-number{font-size:16px;color:var(--ink);display:flex;align-items:center;gap:6px;margin-top:2px}
.brand{right:95px;top:28px;display:flex;align-items:center;gap:8px}
.brand-mark{width:18px;height:18px;background:var(--red)}
.brand-name{font-size:22px;font-weight:500;color:var(--ink);letter-spacing:.3px}
.nav{left:93px;top:74px;display:flex;gap:16px;font-size:12px;font-weight:500;color:var(--ink)}
.nav .active{color:var(--red)}

/* hero */
.hero{left:0;top:107px;width:943px;height:329px;overflow:hidden}
.hero-photo{position:absolute;inset:0;background:linear-gradient(120deg,#cfd4d8 0%,#9ea7ad 35%,#b9c1c6 60%,#dfe3e6 100%)}
.hero-shape{position:absolute;inset:0}
.hero-title{position:absolute;right:98px;top:44px;text-align:right;color:var(--white);font-size:39px;line-height:39px;font-weight:400;text-shadow:0 1px 2px rgba(0,0,0,.35)}
.hero-sub{position:absolute;right:98px;top:148px;text-align:right;color:var(--white);font-size:27px;line-height:36px;font-weight:400;text-shadow:0 1px 2px rgba(0,0,0,.3)}
.dots{position:absolute;left:780px;top:309px;display:flex;gap:5px}
.dots span{width:11px;height:11px;border-radius:50%;background:#eee}
.dots span:first-child{background:#444;border:2px solid #ddd}

/* features */
.feature{width:380px;display:flex;gap:12px}
.feature-icon{flex:none;width:88px;height:88px;border-radius:50%;border:5px solid #111;background:radial-gradient(circle at 50% 40%,#fff 0%,#e3e3e3 100%);display:flex;align-items:center;justify-content:center}
.feature-body{padding-top:7px}
.feature-title{font-size:14px;font-weight:500;color:var(--ink);text-transform:uppercase;margin-bottom:4px}
.feature-title em,.section-title em{font-style:normal;color:var(--red)}
.feature-text{font-size:11px;line-height:13.6px;color:#333}
.more{font-size:11px;color:var(--red);margin-top:4px}

/* about */
.about{left:0;top:722px;width:943px;height:258px;background:var(--panel);border-top:1px solid #ececec}
.about-photo{position:absolute;left:91px;top:20px;width:273px;height:215px;border:3px solid #8a8a8a;background:linear-gradient(160deg,#c7d6e0 0%,#8c9aa4 45%,#b8b0a2 100%)}
.about-copy{position:absolute;left:383px;top:40px;width:462px}
.section-title{font-size:15.5px;font-weight:500;color:var(--ink);text-transform:uppercase;margin-bottom:7px}
.section-text{font-size:11px;line-height:14.7px;color:#444;letter-spacing:.15px}

/* footer */
.footer{left:0;top:980px;width:943px;height:188px;background:var(--footer)}
.footer h4{position:absolute;font-size:13px;font-weight:500;color:var(--white)}
.links{position:absolute;left:97px;top:40px;list-style:none;font-size:10.5px;color:#eee;line-height:21.6px}
.links li::before{content:"› ";}
.quote{position:absolute;left:264px;top:35px;width:160px;font-size:10px;line-height:13.2px;color:#eee;letter-spacing:.3px}
.quote-by{position:absolute;left:350px;top:125px;font-size:9.5px;color:#eee;letter-spacing:.5px}
.btn{position:absolute;background:var(--red);color:var(--white);font-size:11px;border-radius:3px;padding:3px 6px}
.field{position:absolute;left:468px;width:140px;height:17px;background:var(--white);font-size:8.5px;font-style:italic;color:#999;padding:3px 6px}
.badge{position:absolute;left:656px;top:22px;width:54px;height:54px;border-radius:50%;background:#cfcfcf}
.footer-brand{position:absolute;left:658px;top:125px;font-size:20px;font-weight:500;color:#d0d0d0}
.bottom{left:0;top:1168px;width:943px;height:32px;background:var(--red);color:var(--white)}
.copy{position:absolute;left:97px;top:9px;font-size:10px}
.follow{position:absolute;left:660px;top:7px;font-size:13px;font-weight:500;display:flex;align-items:center;gap:6px}
.follow span{width:19px;height:19px;border-radius:50%;background:var(--white)}
</style>
</head>
<body>

<header>
  <div class="abs call">
    <div class="call-label">Call Us Today</div>
    <div class="call-number">
      <svg width="18" height="18" viewBox="0 0 18 18" aria-hidden="true"><circle cx="9" cy="9" r="8" fill="none" stroke="#d9262f" stroke-width="1.6"/><path d="M6 5.2l1.6-.4 1 2-1 .8c.4 1 1.2 1.8 2.2 2.3l.8-1 2 1-.4 1.6c-3 .3-6.5-3.3-6.2-6.3z" fill="#d9262f"/></svg>
      012-555-0147
    </div>
  </div>
  <div class="abs brand"><span class="brand-mark"></span><span class="brand-name">Fenway Lodge Advisory</span></div>
  <nav class="abs nav">
    <span class="active">About Us</span><span>Services</span><span>Working With Us</span><span>Testimonials</span><span>Article Of The Moment</span><span>Client Login</span>
  </nav>
</header>

<section class="abs hero">
  <div class="hero-photo" role="img" aria-label="Consultant standing at a marina railing with moored boats behind"></div>
  <svg class="hero-shape" width="943" height="329" viewBox="0 0 943 329" aria-hidden="true">
    <defs><linearGradient id="heroRed" x1="0" y1="0" x2="1" y2="1"><stop offset="0" stop-color="#e02a33"/><stop offset="1" stop-color="#c51f28"/></linearGradient></defs>
    <polygon points="440,0 458,0 620,166 456,329 438,329 600,166" fill="#2a2a2a"/>
    <polygon points="458,0 943,0 943,329 456,329 620,166" fill="url(#heroRed)"/>
  </svg>
  <h1 class="hero-title">Business can<br>be hard</h1>
  <p class="hero-sub">But We Make<br>detailed<br>analysis of your<br>finances easy</p>
  <div class="dots"><span></span><span></span><span></span><span></span></div>
</section>

<section>
  <div class="abs feature" style="left:93px;top:468px">
    <div class="feature-icon"><svg width="52" height="30" viewBox="0 0 52 30" aria-hidden="true"><rect x="2" y="4" width="28" height="18" rx="9" fill="none" stroke="#d9262f" stroke-width="5"/><rect x="22" y="8" width="28" height="18" rx="9" fill="none" stroke="#d9262f" stroke-width="5"/></svg></div>
    <div class="feature-body">
      <div class="feature-title"><em>Believing in the</em> here and now</div>
      <p class="feature-text">There are many variations of passages<br>of lorem Ipsum available, but the<br>majority have alteration in some form.</p>
      <div class="more">Read More [+]</div>
    </div>
  </div>
  <div class="abs feature" style="left:494px;top:468px">
    <div class="feature-icon"><svg width="50" height="44" viewBox="0 0 50 44" aria-hidden="true"><path d="M3 21L25 3l22 18" fill="none" stroke="#d9262f" stroke-width="4"/><path d="M11 17v25M39 17v25" stroke="#d9262f" stroke-width="4"/></svg></div>
    <div class="feature-body" style="padding-left:16px">
      <div class="feature-title"><em>Your place,</em> in your time</div>
      <p class="feature-text">There are many variations of passages<br>of lorem Ipsum available, but the<br>majority have alteration in some form.</p>
      <div class="more">Read More [+]</div>
    </div>
  </div>
  <div class="abs feature" style="left:93px;top:598px">
    <div class="feature-icon"><svg width="36" height="44" viewBox="0 0 36 44" aria-hidden="true"><rect x="2" y="2" width="32" height="40" rx="3" fill="none" stroke="#d9262f" stroke-width="4"/><path d="M9 12h18M9 19h18M9 26h18M9 33h12" stroke="#d9262f" stroke-width="3.5"/></svg></div>
    <div class="feature-body">
      <div class="feature-title"><em>Monthly</em> billing</div>
      <p class="feature-text">There are many variations of passages<br>of lorem Ipsum available, but<br>majority have alteration in some.</p>
      <div class="more">Read More [+]</div>
    </div>
  </div>
  <div class="abs feature" style="left:494px;top:598px">
    <div class="feature-icon"><svg width="50" height="50" viewBox="0 0 50 50" aria-hidden="true"><path d="M9 17A19 19 0 1 1 8 32" fill="none" stroke="#d9262f" stroke-width="4.5"/><path d="M3 12l7 7 5-9z" fill="#d9262f"/><path d="M25 13v13h10" fill="none" stroke="#d9262f" stroke-width="4.5"/></svg></div>
    <div class="feature-body" style="padding-left:16px">
      <div class="feature-title"><em>We will actually</em> call you back</div>
      <p class="feature-text">There are many variations of<br>passages of lorem Ipsum available,<br>but majority have alteration..</p>
      <div class="more">Read More [+]</div>
    </div>
  </div>
</section>

<section class="abs about">
  <div class="about-photo" role="img" aria-label="Consultant walking along a harbour wharf beside fishing boats"></div>
  <div class="about-copy">
    <h2 class="section-title"><em>Getting to know</em> Fenway Lodge Advisory</h2>
    <p class="section-text">Fenway Lodge Advisory aims to service the needs of its clients by focusing on the present rather than reporting on historical figures. We recognise that business owners benefit from regular contact with their accountant. One who undertakes a hands on approach in working with business owners to improve their business.</p>
    <h2 class="section-title" style="margin-top:22px"><em>Fenway Lodge</em> Advisory difference</h2>
    <p class="section-text" style="letter-spacing:0">Not all Accountants are created equally … the Fenway Lodge Advisory difference. Fenway Lodge Advisory takes pride in not following the status quo, the following points are just some of the unique benefits you will experience when working with us.</p>
  </div>
</section>

<footer class="abs footer">
  <h4 style="left:97px;top:19px">Quick Links</h4>
  <ul class="links">
    <li>About Us</li><li>Services</li><li>Working With Us</li><li>Testimonials</li><li>Article Of The Moment</li><li>Client Login</li>
  </ul>
  <h4 style="left:265px;top:19px">Testimonials</h4>
  <p class="quote">“ Lorem ipsum dolor sit amet tetuer adipiscing elit, sed diam nonum sum ipsum Lorem ipsum dolor sit amet, tetuer adipiscing elit, sed diam nonum ”</p>
  <div class="quote-by">Lorem, <small>Director</small></div>
  <div class="btn" style="left:360px;top:147px">View All »</div>
  <h4 style="left:468px;top:19px">Quick Contact</h4>
  <div class="field" style="top:47px">Enter Your Name</div>
  <div class="field" style="top:68px">Enter Your Email</div>
  <div class="field" style="top:89px">Enter Your Phone</div>
  <div class="field" style="top:109px;height:35px">Message</div>
  <div class="btn" style="left:518px;top:147px">Send Message »</div>
  <div class="badge" aria-hidden="true"></div>
  <div class="footer-brand">Fenway Lodge Advisory</div>
</footer>

<div class="abs bottom">
  <div class="copy">© 2013 Fenway Lodge Advisory. All Rights Reserved.</div>
  <div class="follow">Follow Us On: <span></span><span></span><span></span></div>
</div>

</body>
</html>
```